Website for new dental office

I am Dr. Colin Marsh and am building a new dental practice. I specialize in general dentistry. I am young and have a higher end dental practice incorporating very new technologies and would like my website to reflect that. As many dental patients are older, the website must be very easy to navigate. I would like patients to be able to request appointments, and will eventually add on patient information forms (the health history, etc, that you normally fill out in the practice) from my practice management software, so leave an area for that.

Industry/Entity Type

Building

```html
<!DOCTYPE html>
<html lang="en">
<head>
<meta charset="utf-8">
<title>Family Dentist – Dr. Colin Marsh</title>
<link rel="stylesheet" href="https://fonts.googleapis.com/css2?family=Yanone+Kaffeesatz:wght@300;400;700&family=Arimo:wght@400;700&display=swap">
<style>
:root{
  --blue:#1a80d2;
  --blue-dark:#136bb4;
  --blue-band:#1b7dcc;
  --card-1:#3a9fe2;
  --card-2:#2d8ed8;
  --card-3:#2e6bc1;
  --card-4:#2e48a6;
  --ink:#444;
  --muted:#9a9a9a;
  --soft:#f1f1f1;
  --line:#e2e2e2;
  --footer:#3e3e3e;
  --footer-deep:#2d2d2d;
  --footer-row:#4a4a4a;
  --white:#fff;
}
*{margin:0;padding:0;box-sizing:border-box}
html,body{width:811px;height:1200px;overflow:hidden}
body{position:relative;background:var(--white);font-family:"Arimo",Arial,sans-serif;color:var(--ink);font-size:8px}
.abs{position:absolute}
.head-font{font-family:"Yanone Kaffeesatz",sans-serif}

/* top bar */
.topbar{left:411px;top:0;width:243px;height:12px;background:#ececec;display:flex;align-items:center;gap:6px;padding:0 6px;font-size:6px;color:#555}
.topbar .dot{width:6px;height:6px;border-radius:50%;background:#777}
.brand{left:165px;top:12px;display:flex;align-items:center;gap:8px}
.brand .mark{width:40px;height:40px;border-radius:50%;background:var(--blue)}
.brand span{font-family:"Yanone Kaffeesatz",sans-serif;font-size:25px;color:var(--blue);font-weight:400}
.nav{left:358px;top:31px;height:29px;display:flex;font-family:"Yanone Kaffeesatz",sans-serif;font-size:11px;color:#666}
.nav a{display:flex;align-items:center;padding:0 6px;color:inherit;text-decoration:none}
.nav a.active{background:var(--blue);color:var(--white)}

/* hero */
.band{left:0;top:61px;width:811px;height:203px;background:var(--blue-band)}
.hero{left:157px;top:61px;width:497px;height:143px;background:linear-gradient(90deg,#9aa0a6,#c7ccd1 55%,#e4e6e8)}
.hero-cap{left:169px;top:110px;width:201px;height:53px;background:rgba(80,80,80,.7);padding:3px 7px;color:var(--white);font-family:"Yanone Kaffeesatz",sans-serif;line-height:1}
.hero-cap .l1{font-size:17px;font-weight:300}
.hero-cap .l2{font-size:20px;font-weight:700}
.hero-cap .l3{font-size:12px;font-weight:300;color:#ddd}

.appt{left:157px;top:204px;width:497px;height:146px;background:var(--blue);color:var(--white)}
.tab-l{left:0;top:0;width:252px;height:30px;background:var(--blue-dark);font-family:"Yanone Kaffeesatz",sans-serif;font-size:14px;padding:8px 13px}
.tab-r{left:252px;top:0;width:245px;height:30px;background:var(--white);color:var(--blue);font-family:"Yanone Kaffeesatz",sans-serif;font-size:14px;padding:7px 14px;display:flex;align-items:center;gap:7px}
.col-title{font-family:"Yanone Kaffeesatz",sans-serif;font-size:12px;display:flex;align-items:center;gap:5px}
.hours{left:14px;top:70px;width:130px}
.hours div{display:flex;justify-content:space-between;font-size:7px;padding:5px 0 6px;border-bottom:1px solid rgba(255,255,255,.6)}
.field{height:16px;border:1px solid var(--white);font-size:7px;padding:3px 4px;background:var(--blue)}
.btn{background:var(--white);color:#444;font-size:7px;height:13px;display:flex;align-items:center;justify-content:center}

/* services */
.h-sec{font-family:"Yanone Kaffeesatz",sans-serif;font-size:17px;color:#555;font-weight:300}
.h-sec b{color:var(--blue);font-weight:700}
.rule{left:157px;top:381px;width:497px;height:1px;background:var(--line)}
.rule-blue{left:188px;top:379px;width:59px;height:2px;background:var(--blue)}
.card{top:401px;width:123px;height:171px}
.card .photo{height:76px;background:linear-gradient(135deg,#e9d3c7,#c98f86)}
.card .body{height:79px;padding:8px 10px;color:var(--white)}
.card .body h3{font-family:"Yanone Kaffeesatz",sans-serif;font-size:15px;font-weight:300;margin-bottom:5px}
.card .body h3 b{font-weight:700}
.card .body p{font-size:6.5px;line-height:1.6}
.card .more{height:16px;background:#4b4b4b;color:#ddd;font-size:6.5px;padding:4px 11px}

.soft{left:0;top:630px;width:811px;height:340px;background:var(--soft)}
.partners{left:157px;top:596px;width:497px;height:65px;background:var(--white);border:1px solid var(--line)}
.arrow{width:13px;height:14px;background:var(--blue);display:flex;align-items:center;justify-content:center}
.badge{top:15px;width:76px;height:34px;background:#dde7ef;border-radius:3px}

/* about */
.acc{left:157px;width:287px;background:var(--white)}
.acc-head{display:flex;align-items:center;gap:10px;font-family:"Yanone Kaffeesatz",sans-serif;font-size:14px;color:#555;padding:0 7px}
.acc-head b{color:var(--blue)}
.plus{width:11px;height:11px;background:var(--blue);color:var(--white);font-size:9px;display:flex;align-items:center;justify-content:center;font-family:Arial,sans-serif}
.acc p{font-size:6.5px;color:var(--muted);line-height:1.6;margin:0 25px 8px 25px}

.quote{left:460px;width:194px;background:var(--white);padding:8px 10px 8px 20px;font-size:8px;line-height:1.6;color:#444}
.qm{color:var(--blue);font-size:14px;font-family:Georgia,serif}
.person{left:462px;display:flex;gap:6px;align-items:center;font-size:6.5px}
.avatar{width:21px;height:21px;background:linear-gradient(#b9a89c,#6e6e74)}
.role{left:461px;font-size:6.5px;color:var(--muted)}

/* footer */
.footer{left:0;top:970px;width:811px;height:190px;background:var(--footer);color:#ddd}
.f-h{font-family:"Yanone Kaffeesatz",sans-serif;font-size:15px;font-weight:300;color:var(--white)}
.f-list{list-style:none;font-size:7px}
.f-list li{height:21px;display:flex;align-items:center;gap:10px;border-bottom:1px solid #4d4d4d;padding-left:1px}
.f-list li::before{content:"›";color:var(--blue);font-size:11px}
.post{display:flex;gap:8px;font-size:6.5px;line-height:1.5}
.post .ico{width:15px;height:15px;background:#3a9fe2;flex:none}
.post-time{font-size:6px;color:#3a9fe2;margin:4px 0 10px}
.contact-row{width:124px;background:var(--footer-row);font-size:6.5px;display:flex;align-items:center;gap:9px;padding:0 8px;margin-bottom:2px}
.bottom{left:0;top:1160px;width:811px;height:40px;background:var(--footer-deep);color:#ddd;font-size:7px;padding:17px 158px}
</style>
</head>
<body>

<div class="abs topbar"><span>Some Lorem Ipsum</span><span>EN</span><i class="dot"></i><i class="dot"></i><i class="dot"></i><i class="dot"></i><span>✉ info@marshdental.com</span><span>(912) 555-0148</span></div>
<div class="abs brand"><i class="mark"></i><span>Family Dentist</span></div>
<nav class="abs nav"><a class="active">Home</a><a>About Us</a><a>The Practice</a><a>Are of Expertiese</a><a>Appointment</a><a>Contact</a></nav>

<div class="abs band"></div>
<div class="abs hero" role="img" aria-label="Photo of a smiling dentist with a patient in a modern treatment room"></div>
<div class="abs hero-cap"><div class="l1">Welcome to Family Dentist</div><div class="l2">PROIN GRAVIDA NIBH</div><div class="l3">lorem quis bibendum auctor, nisi elit</div></div>

<section class="abs appt">
  <div class="abs tab-l">Make an Appointment</div>
  <div class="abs tab-r"><svg width="13" height="12" viewBox="0 0 13 12"><rect x="0" y="2" width="13" height="10" rx="1" fill="currentColor"/><rect x="4" y="0" width="5" height="3" fill="none" stroke="currentColor"/><path d="M6.5 4v6M3.5 7h6" stroke="#fff" stroke-width="1.6"/></svg>For Emergency Cases</div>

  <div class="abs col-title" style="left:12px;top:42px"><svg width="9" height="9"><circle cx="4.5" cy="4.5" r="4" fill="#fff"/><path d="M4.5 2v3h2" stroke="#1a80d2" fill="none"/></svg>Working Time</div>
  <div class="abs hours">
    <div><span>Monday – Friday</span><span>8.00 – 17.00</span></div>
    <div><span>Saturday</span><span>9.30 – 17.30</span></div>
    <div style="border:0"><span>Sunday</span><span>9.30 – 15.00</span></div>
  </div>

  <div class="abs col-title" style="left:157px;top:42px"><svg width="9" height="9"><rect x=".5" y="1.5" width="8" height="7" fill="#fff"/></svg>Doctors Timetable</div>
  <p class="abs" style="left:158px;top:66px;width:108px;font-size:7px;line-height:1.35">Lorem ipsum dolor sit amet, consectetur adipisicing elit, sed do eiusmod tempor incididunt ut labore et dolore.</p>
  <div class="abs btn" style="left:193px;top:120px;width:66px">View Timetable</div>

  <div class="abs col-title" style="left:280px;top:42px"><svg width="9" height="9"><rect x=".5" y="1.5" width="8" height="7" fill="#fff"/></svg>Booking a Visit</div>
  <div class="abs field" style="left:280px;top:68px;width:89px">Select Department</div>
  <div class="abs field" style="left:381px;top:68px;width:90px">Your Phone</div>
  <div class="abs field" style="left:280px;top:94px;width:89px">Full Name</div>
  <div class="abs field" style="left:381px;top:94px;width:90px">mm/dd/yyyy</div>
  <div class="abs btn" style="left:405px;top:120px;width:66px">Send</div>
</section>

<h2 class="abs h-sec" style="left:157px;top:359px">About <b>OUR SERVICES</b></h2>
<div class="abs rule"></div><div class="abs rule-blue"></div>

<article class="abs card" style="left:157px"><div class="photo" role="img" aria-label="Photo of a smiling young woman"></div><div class="body" style="background:var(--card-1)"><h3><b>Cosmetic</b> Dentistry</h3><p>Lorem Ipsum. Proin gravida nibh vel velit auctor aliquet. Aenean sollicitudin, lorem quis bibendum auctor, nisi elit consequat ipsum,</p></div><div class="more">Read more →</div></article>
<article class="abs card" style="left:282px"><div class="photo" role="img" aria-label="Close-up photo of a bright smile during a check-up"></div><div class="body" style="background:var(--card-2)"><h3><b>Tooth</b> Whitening</h3><p>Lorem Ipsum. Proin gravida nibh vel velit auctor aliquet. Aenean sollicitudin, lorem quis bibendum auctor, nisi elit consequat ipsum,</p></div><div class="more">Read more →</div></article>
<article class="abs card" style="left:407px"><div class="photo" role="img" aria-label="Close-up photo of a smile with white teeth"></div><div class="body" style="background:var(--card-3)"><h3><b>Smile</b> Makeover</h3><p>Lorem Ipsum. Proin gravida nibh vel velit auctor aliquet. Aenean sollicitudin, lorem quis bibendum auctor, nisi elit consequat ipsum,</p></div><div class="more">Read more →</div></article>
<article class="abs card" style="left:531px"><div class="photo" style="background:linear-gradient(135deg,#e4e4e4,#a9a9a9)" role="img" aria-label="Photo of a dental implant model"></div><div class="body" style="background:var(--card-4)"><h3><b>Dental</b> Implants</h3><p>Lorem Ipsum. Proin gravida nibh vel velit auctor aliquet. Aenean sollicitudin, lorem quis bibendum auctor, nisi elit consequat ipsum,</p></div><div class="more">Read more →</div></article>

<div class="abs soft"></div>
<div class="abs partners">
  <div class="abs arrow" style="left:9px;top:26px"><svg width="5" height="7"><path d="M4 0L0 3.5 4 7" fill="none" stroke="#fff" stroke-width="1.5"/></svg></div>
  <div class="abs badge" style="left:35px"></div>
  <div class="abs badge" style="left:139px"></div>
  <div class="abs badge" style="left:245px"></div>
  <div class="abs badge" style="left:351px"></div>
  <div class="abs arrow" style="left:470px;top:26px"><svg width="5" height="7"><path d="M1 0L5 3.5 1 7" fill="none" stroke="#fff" stroke-width="1.5"/></svg></div>
</div>

<h2 class="abs h-sec" style="left:161px;top:690px;font-size:14px">About <b>US</b></h2>
<div class="abs acc" style="top:714px;height:146px">
  <div class="acc-head" style="padding-top:8px;font-size:20px"><span class="plus">-</span><span style="color:var(--blue)">Dr. <b>Colin Marsh</b></span></div>
  <p style="margin-top:6px">Lorem Ipsum. Proin gravida nibh vel velit auctor aliquet. Aenean sollicitudin, lorem quis bibendum auctor, nisi elit consequat ipsum, nec sagittis sem nibh id elit.</p>
  <p>Duis sed odio sit amet nibh vulputate cursus a sit amet mauris. Morbi accumsan ipsum velit. Nam nec tellus a odio tincidunt auctor a ornare odio. Sed non mauris vitae erat consequat auctor eu in elit.</p>
  <p>Class aptent taciti sociosqu ad litora torquent per conubia nostra, per inceptos himenaeos. Mauris in erat justo. Nullam ac urna eu felis dapibus condimentum sit amet a augue. Sed non neque elit. Sed ut imperdiet nisi. Proin condimentum</p>
</div>
<div class="abs acc" style="top:869px;height:29px;display:flex"><div class="acc-head"><span class="plus">+</span><span>Essential <b>FACTS</b></span></div></div>
<div class="abs acc" style="top:906px;height:29px;display:flex"><div class="acc-head"><span class="plus">+</span><span>Core <b>VALUES</b></span></div></div>

<h2 class="abs h-sec" style="left:460px;top:690px;font-size:14px">Our Client <b>TESTIMONIALS</b></h2>
<blockquote class="abs quote" style="top:714px;height:80px"><span class="qm">“</span> Lorem Ipsum. Proin gravida nibh vel velit auctor aliquet. Aenean sollicitudin, lorem quis bibendum auctor, nisi elit consequat ipsum, nec sagittis sem nibh id elit. Duis sed odio sit amet nibh vulputate cursus a sit amet mauris. <span class="qm">”</span></blockquote>
<div class="abs person" style="top:797px"><i class="avatar" role="img" aria-label="Client portrait"></i><span style="margin-left:4px">Mark Dalton</span></div>
<div class="abs role" style="top:820px">Businessman, Colorado</div>
<blockquote class="abs quote" style="top:842px;height:56px"><span class="qm">“</span> Lorem Ipsum. Proin gravida nibh vel velit auctor aliquet. Aenean sollicitudin, lorem quis bibendum auctor, nisi elit consequat ipsum. <span class="qm">”</span></blockquote>
<div class="abs person" style="top:907px"><i class="avatar" role="img" aria-label="Client portrait"></i><span style="margin-left:4px">Priya Anand</span></div>
<div class="abs role" style="top:930px">House Wife, England</div>
<div class="abs" style="left:633px;top:927px;display:flex;gap:1px"><i style="width:9px;height:9px;background:#ddd;font-size:6px;text-align:center;font-style:normal">‹</i><i style="width:9px;height:9px;background:#ddd;font-size:6px;text-align:center;font-style:normal">›</i></div>

<footer class="abs footer">
  <h3 class="abs f-h" style="left:158px;top:13px">Quick Links</h3>
  <ul class="abs f-list" style="left:158px;top:30px;width:75px"><li>Home</li><li>About Us</li><li>The Practice</li><li>Are of Expertiese</li><li>Appointment</li><li>Contact</li></ul>
  <h3 class="abs f-h" style="left:252px;top:13px">More</h3>
  <ul class="abs f-list" style="left:252px;top:30px;width:100px"><li>Lorem Ipsum Proin gra</li><li>nibh velit auctor aliqut</li><li>Aenean sollicitudin</li><li>bibendum auctor, nisi elit</li><li>ipsum, nec sagittis sem</li><li>Duis sed odio sit amet</li></ul>
  <h3 class="abs f-h" style="left:378px;top:13px">News Feed</h3>
  <div class="abs" style="left:378px;top:33px;width:118px">
    <div class="post"><i class="ico"></i><span>Proin gravida nibh vel velit auctor aliquet. Aenean sollicitudin, lorem quis bibendum auctor, nisi elit consequat ipsum, nec sagittis sem http://lnk.example/dq4Rz aeneage.</span></div>
    <div class="post-time">Posted 11 hours ago</div>
    <div class="post"><i class="ico"></i><span>Proin gravida nibh vel velit auctor aliquet. Aenean sollicitudin, lorem quis bibendum auctor, nisi elit consequat ipsum, nec sagittis sem http://lnk.example/dq4Rz aeneage.</span></div>
    <div class="post-time">Posted 11 hours ago</div>
  </div>
  <h3 class="abs f-h" style="left:534px;top:13px">Contact Details</h3>
  <div class="abs" style="left:530px;top:34px">
    <div class="contact-row" style="height:24px"><svg width="6" height="8"><path d="M3 8C0 4 0 3 0 3a3 3 0 016 0s0 1-3 5z" fill="#fff"/></svg><span>Orchard Lane 18,<br>Riverton</span></div>
    <div class="contact-row" style="height:24px"><svg width="7" height="7"><path d="M1 0l2 2-1 1 2 2 1-1 2 2-1 1C3 7 0 4 0 1z" fill="#fff"/></svg><span>Phone: +123 45 678-901</span></div>
    <div class="contact-row" style="height:24px"><svg width="8" height="6"><rect width="8" height="6" fill="#fff"/><path d="M0 0l4 3 4-3" stroke="#4a4a4a" fill="none"/></svg><span>Email:info@marshdental.com</span></div>
  </div>
</footer>
<div class="abs bottom">©2013 &nbsp;Dr. Colin Marsh. All right reserved.</div>

</body>
</html>
```